Business Card and Stationary Design

After the successful redesign of our logo we are wanting to follow suite and create a new business card and stationary design!

New Logo is attached, information required on the business card should contain a mixture of the following but layout/arrangement is up to the designer.

Happy if the national provider number and abn are on the back, and happy for them to be smaller than the rest.

I am also happy to receive single sided or weird and wonderful designs.

Name
Title
National Provider Number 7291
ABN 53 219 864 317
Level 3, 42 Marlow Street
Kelvale NSW 2306
Ph: 1300 987 214
Mobile: 0432 785 619
name@ferngatebuild.com.au
www.ferngatebuild.com.au

Target Market(s)

Professionals, Peers, Students, Suppliers...

Industry/Entity Type

Construction

Contact Information for Business Card

Listed in project description

Font styles to use
Other font styles liked:
• Century Gothic

Colors
0455a3
3176b5
ffffff

Requirements
Must have
• Professional Design, same color scheme as our logo
Nice to have
• Something that sets our apart from everyone else would be fantastic, open to size and shape and layout options, as long as they present professionally.
• Open to raised/embossed text, alternative materials, custom sizes, clear material
Should not have
• The color orange

```html
<!DOCTYPE html>
<html lang="en">
<head>
<meta charset="utf-8">
<title>Ferngatebuild business card</title>
<link rel="stylesheet" href="https://fonts.googleapis.com/css2?family=Questrial&display=swap">
<style>
  :root {
    --brand-blue: #2a4fae;
    --brand-blue-deep: #1f3f98;
    --paper: #ffffff;
    --ink-grey: #6d6d6d;
    --rule-grey: #a7a7a7;
    --stage: #ecebe8;
    --band-edge: #e2e2e2;
  }
  * { margin: 0; padding: 0; box-sizing: border-box; }
  html, body { width: 1200px; height: 1023px; overflow: hidden; }
  body {
    background: var(--stage);
    font-family: "Questrial", "Century Gothic", sans-serif;
    position: relative;
  }
  .card {
    position: absolute;
    left: 200px;
    width: 800px;
    height: 457px;
    border-radius: 4px;
    box-shadow: 0 6px 18px rgba(0,0,0,.18);
    overflow: hidden;
  }
  .card--front { top: 34px; background: var(--paper); }
  .card--back  { top: 532px; background: var(--brand-blue); }

  /* front */
  .wordmark {
    position: absolute;
    color: var(--brand-blue);
    font-size: 40px;
    letter-spacing: -0.5px;
    display: flex;
    align-items: center;
    gap: 12px;
    white-space: nowrap;
  }
  .wordmark__mark { width: 26px; height: 26px; background: var(--brand-blue); flex: none; }
  .card--front .wordmark { left: 40px; top: 40px; }
  .registration {
    position: absolute;
    right: 40px; top: 42px;
    color: var(--ink-grey);
    font-size: 17px;
    line-height: 1.35;
    text-align: right;
  }
  .name-band {
    position: absolute;
    left: 300px; right: 0; top: 150px;
    height: 92px;
    background: var(--brand-blue);
    color: var(--paper);
    text-align: right;
    padding: 10px 40px 0 0;
  }
  .name-band::before {
    content: "";
    position: absolute;
    left: 0; right: 0; top: -8px;
    height: 3px;
    background: var(--rule-grey);
  }
  .name-band__name { font-size: 36px; letter-spacing: 1px; text-transform: uppercase; line-height: 1.1; }
  .name-band__title { font-size: 22px; }
  .address {
    position: absolute;
    left: 40px; bottom: 40px;
    color: var(--ink-grey);
    font-size: 22px;
    line-height: 1.35;
  }
  .contact {
    position: absolute;
    right: 40px; top: 262px;
    list-style: none;
    color: var(--ink-grey);
    font-size: 20px;
    line-height: 1.5;
    text-align: right;
  }
  .contact li { display: flex; justify-content: flex-end; align-items: center; gap: 12px; }
  .contact svg { width: 16px; height: 16px; fill: var(--brand-blue); flex: none; }
  .contact .contact__gap { margin-top: 28px; }

  /* back */
  .feature-band {
    position: absolute;
    left: 0; right: 0; top: 120px;
    height: 170px;
    background: var(--paper);
    border-bottom: 8px solid var(--band-edge);
  }
  .card--back .wordmark { left: 200px; top: 60px; font-size: 56px; }
  .card--back .wordmark__mark { width: 34px; height: 34px; }
  .back-url {
    position: absolute;
    left: 0; right: 0; bottom: 50px;
    text-align: center;
    color: var(--paper);
    font-size: 24px;
    letter-spacing: .5px;
  }
</style>
</head>
<body>
  <section class="card card--front" aria-label="Business card front">
    <div class="wordmark"><span class="wordmark__mark"></span>ferngatebuild</div>
    <p class="registration">National Provider Number 7291<br>ABN 53 219 864 317</p>
    <div class="name-band">
      <p class="name-band__name">Corin Halvey</p>
      <p class="name-band__title">Executive Manager</p>
    </div>
    <p class="address">Level 3, 42 Marlow Street<br>Kelvale NSW 2306</p>
    <ul class="contact">
      <li>1300 987 214
        <svg viewBox="0 0 16 16" aria-hidden="true"><path d="M3 1l3 3-2 2c1 2 4 5 6 6l2-2 3 3-2 2C7 15 1 9 1 3z"/></svg></li>
      <li>0432 785 619
        <svg viewBox="0 0 16 16" aria-hidden="true"><rect x="4" y="1" width="8" height="14" rx="2"/></svg></li>
      <li class="contact__gap">name@ferngatebuild.com.au
        <svg viewBox="0 0 16 16" aria-hidden="true"><path d="M1 3h14v10H1z M1 3l7 6 7-6"/></svg></li>
      <li>www.ferngatebuild.com.au
        <svg viewBox="0 0 16 16" aria-hidden="true"><circle cx="8" cy="8" r="7"/></svg></li>
    </ul>
  </section>

  <section class="card card--back" aria-label="Business card back">
    <div class="feature-band">
      <div class="wordmark"><span class="wordmark__mark"></span>ferngatebuild</div>
    </div>
    <p class="back-url">www.ferngatebuild.com.au</p>
  </section>
</body>
</html>
```